Transform this table

Please make a 2 page A4 handout from this boring table into an engaging design. The front page can be simple and engaging (a summary of the back where all the detail lives)

Target Market(s)

Business

Requirements
Must have
• Clarity. And impact.
Nice to have
• Icons

```html
<!DOCTYPE html>
<html lang="en">
<head>
<meta charset="utf-8">
<title>Safety Culture Maturity Ladder</title>
<link href="https://fonts.googleapis.com/css2?family=Figtree:wght@400;500;600;700;800&family=Montserrat:wght@400;500;600;700;800;900&display=swap" rel="stylesheet">
<style>
:root{
  --stage:#3a3a3a;
  --stage-title:#6b6b6b;
  --blue:#1b4fa2;
  --blue-dark:#0e3571;
  --crimson:#d31f54;
  --crimson-dark:#93163c;
  --orange:#f7891f;
  --orange-dark:#df7420;
  --teal:#3589b6;
  --teal-dark:#2b76a2;
  --charcoal:#2f2f2f;
  --charcoal-dark:#222222;
  --headline:#d41f52;
  --sub:#2a8bb5;
  --rule:#9e9e9e;
  --band:#e6e6e6;
  --ink:#333333;
  --ghost:#e9e9e9;
  --white:#ffffff;
}
*{margin:0;padding:0;box-sizing:border-box}
html,body{width:817px;height:1200px;overflow:hidden}
body{background:var(--stage);font-family:"Montserrat",Arial,sans-serif;position:relative;color:var(--ink)}
.board-title{position:absolute;top:30px;left:0;width:817px;text-align:center;font-weight:900;font-size:50px;letter-spacing:-0.5px;color:var(--stage-title);line-height:1}

.page{position:absolute;left:60px;width:697px;background:var(--white);overflow:hidden}
.page--front{top:124px;height:493px}
.page--back{top:661px;height:491px;border:4px solid var(--band)}

/* front */
.front-header{height:63px;background:linear-gradient(90deg,#1a86c8,#1e3f8f);display:flex;align-items:center;justify-content:center}
.front-header h1{color:var(--white);font-weight:800;font-size:32.5px;letter-spacing:0.2px}
.progress-title{position:absolute;top:83px;left:0;width:697px;text-align:center;font-weight:800;font-size:20.5px;color:var(--headline)}
.progress-sub{position:absolute;top:119px;left:0;width:697px;text-align:center;font-weight:500;font-size:13.5px;color:var(--sub)}
.ladder-art{position:absolute;left:0;top:0}
.stage-label{position:absolute;width:140px;margin-left:-70px;text-align:center;font-weight:800;font-size:11.5px}
.step{position:absolute;bottom:49px;width:118px;color:var(--white);text-align:center}
.step__head{height:35px;display:flex;align-items:center;justify-content:center;font-weight:700;font-size:10.5px;line-height:1.1;padding:0 4px}
.step__quote{font-weight:500;font-size:9.3px;line-height:1.25;padding:9px 8px 0}
.step__text{font-weight:400;font-size:9.3px;line-height:1.25;padding:12px 10px 0}
.step--vulnerable{left:40px;height:71px;background:var(--blue)}
.step--vulnerable .step__head{background:var(--blue-dark)}
.step--vulnerable .step__quote{padding-top:4px}
.step--reactive{left:165px;height:114px;background:var(--crimson)}
.step--reactive .step__head{background:var(--crimson-dark)}
.step--compliant{left:290px;height:153px;background:var(--orange)}
.step--compliant .step__head{background:var(--orange-dark)}
.step--proactive{left:414px;height:196px;background:var(--teal)}
.step--proactive .step__head{background:var(--teal-dark)}
.step--resilient{left:539px;height:240px;background:var(--charcoal)}
.step--resilient .step__head{background:var(--charcoal-dark)}
.front-footer{position:absolute;left:0;top:454px;width:697px;height:28px;background:var(--band);display:flex;align-items:center;justify-content:center;font-size:9.3px;color:#333}

/* back */
.back-title{position:absolute;top:8px;left:0;width:689px;text-align:center;font-weight:800;font-size:34px;color:var(--ghost);white-space:nowrap}
.trait-col{position:absolute;top:58px;width:128px}
.trait-col--vulnerable{left:16px;--c:var(--blue)}
.trait-col--reactive{left:154px;--c:var(--crimson)}
.trait-col--compliant{left:282px;--c:var(--orange)}
.trait-col--proactive{left:422px;--c:var(--teal)}
.trait-col--resilient{left:553px;--c:var(--charcoal);width:128px}
.bullets{list-style:none;font-family:"Figtree",Arial,sans-serif;font-size:7.6px;line-height:1.35}
.bullets li{position:relative;padding-left:7px}
.bullets li::before{content:"•";position:absolute;left:0;color:var(--c)}
.bullets ul{list-style:none;padding-left:7px}
.bullets .lead{color:var(--c);font-weight:700}
.trait-col--resilient .lead{color:var(--charcoal);font-weight:700}
.trait-col--resilient .bullets li::before{color:var(--charcoal)}
.summary{font-family:"Figtree",Arial,sans-serif;font-weight:700;font-size:7.8px;color:var(--c);margin-top:7px;padding-left:2px;line-height:1.2}

.tier-art{position:absolute;left:0;top:0}
.tier{position:absolute;width:128px;color:var(--white);--c:var(--white)}
.tier__name{position:absolute;width:128px;text-align:center;font-weight:800;font-size:10px}
.tier .bullets{position:absolute;left:8px;width:116px;font-size:7.5px;line-height:1.32}
.tier .bullets b{font-weight:700}
.tier--vulnerable{left:15px}
.tier--reactive{left:147px}
.tier--compliant{left:280px}
.tier--proactive{left:412px}
.tier--resilient{left:545px}
</style>
</head>
<body>

<svg width="0" height="0" style="position:absolute" aria-hidden="true">
  <defs>
    <symbol id="icon-shield" viewBox="0 0 24 24"><path d="M12 3 L19 6 V11 C19 16 16 19.5 12 21 C8 19.5 5 16 5 11 V6 Z" fill="none" stroke="currentColor" stroke-width="1.8" stroke-linejoin="round"/><path d="M9.5 9.5 L14.5 14.5 M14.5 9.5 L9.5 14.5" stroke="currentColor" stroke-width="1.8" stroke-linecap="round"/></symbol>
    <symbol id="icon-cycle" viewBox="0 0 24 24"><g fill="none" stroke="currentColor" stroke-width="2.2" stroke-linecap="round" stroke-linejoin="round"><path d="M18.5 9 A7 7 0 0 0 5.6 8.5"/><path d="M5.5 15 A7 7 0 0 0 18.4 15.5"/><path d="M18.8 5 V9.2 H14.6"/><path d="M5.2 19 V14.8 H9.4"/></g></symbol>
    <symbol id="icon-doc" viewBox="0 0 24 24"><g fill="none" stroke="currentColor" stroke-width="1.6" stroke-linecap="round" stroke-linejoin="round"><rect x="5.5" y="3" width="11" height="15" rx="1"/><path d="M8 7 H14 M8 10 H14 M8 13 H11"/><circle cx="17" cy="17" r="4"/><path d="M15.3 17 L16.6 18.3 L18.8 15.8"/></g></symbol>
    <symbol id="icon-bulb" viewBox="0 0 24 24"><g fill="none" stroke="currentColor" stroke-width="1.6" stroke-linecap="round" stroke-linejoin="round"><path d="M9 16 C9 14 7 13 7 10 A5 5 0 0 1 17 10 C17 13 15 14 15 16 Z"/><path d="M9.5 18.5 H14.5 M10.2 20.8 H13.8"/><path d="M12 2 V3.4 M4.8 4.8 L5.8 5.8 M19.2 4.8 L18.2 5.8 M2.5 10 H3.9 M20.1 10 H21.5"/><path d="M10.5 11.5 L12 13.5 L13.5 11.5 M12 13.5 V16"/></g></symbol>
    <symbol id="icon-converge" viewBox="0 0 24 24"><g fill="none" stroke="currentColor" stroke-width="1.6" stroke-linecap="round" stroke-linejoin="round"><path d="M10 5.5 V18.5 M12 3.5 V20.5 M14 5.5 V18.5"/><path d="M2.5 12 H8 M5.8 9.8 L8 12 L5.8 14.2"/><path d="M21.5 12 H16 M18.2 9.8 L16 12 L18.2 14.2"/></g></symbol>
  </defs>
</svg>

<div class="board-title">TRANSFORM THIS TABLE</div>

<!-- Front page -->
<section class="page page--front">
  <header class="front-header"><h1>SAFETY CULTURE MATURITY LADDER</h1></header>
  <div class="progress-title">IMPROVING SAFETY CULTURE</div>
  <div class="progress-sub">Increasing accountability &amp; reliability</div>

  <svg class="ladder-art" width="697" height="493" viewBox="0 0 697 493" aria-hidden="true">
    <line x1="167" y1="113" x2="528" y2="113" stroke="var(--rule)" stroke-width="2.5"/>
    <path d="M527 107 L538 113 L527 119 Z" fill="var(--rule)"/>
    <line x1="93" y1="305" x2="594" y2="145" stroke="#a8a8a8" stroke-width="1.6" stroke-dasharray="6 4"/>
    <path d="M41 366 H157 V326 M157 322 H282 V284 M282 282 H407 V244 M407 240 H532 V208" fill="none" stroke="#555" stroke-width="1.3" stroke-dasharray="5 3"/>
    <path d="M154 328 L157 321 L160 328 Z M279 286 L282 279 L285 286 Z M404 246 L407 239 L410 246 Z M529 210 L532 203 L535 210 Z" fill="var(--blue)"/>
    <g color="var(--white)">
      <circle cx="93" cy="305" r="22" fill="var(--blue)"/><use href="#icon-shield" x="79" y="291" width="28" height="28"/>
      <circle cx="221" cy="264" r="22" fill="var(--crimson)"/><use href="#icon-cycle" x="207" y="250" width="28" height="28"/>
      <circle cx="347" cy="226" r="22" fill="var(--orange)"/><use href="#icon-doc" x="333" y="212" width="28" height="28"/>
      <circle cx="465" cy="186" r="22" fill="var(--teal)"/><use href="#icon-bulb" x="451" y="172" width="28" height="28"/>
      <circle cx="594" cy="145" r="22" fill="var(--charcoal)"/><use href="#icon-converge" x="580" y="131" width="28" height="28"/>
    </g>
  </svg>

  <div class="stage-label" style="left:95px;top:333px;color:var(--blue-dark)">VULNERABLE</div>
  <div class="stage-label" style="left:223px;top:297px;color:var(--crimson)">REACTIVE</div>
  <div class="stage-label" style="left:348px;top:257px;color:var(--orange)">COMPLIANT</div>
  <div class="stage-label" style="left:467px;top:218px;color:var(--teal)">PROACTIVE</div>
  <div class="stage-label" style="left:597px;top:179px;color:var(--charcoal)">RESILIENT</div>

  <div class="step step--vulnerable"><div class="step__head">TOXIC / NO CARE CULTURE</div><p class="step__quote" style="font-weight:400">“Accidents Happen”</p></div>
  <div class="step step--reactive"><div class="step__head">BLAME<br>CULTURE</div><p class="step__quote">“It was an accident!”</p><p class="step__text">Wake management &amp; control high risks</p></div>
  <div class="step step--compliant"><div class="step__head">COMPLIANCE<br>CULTURE</div><p class="step__quote">“Incidents have causes”</p><p class="step__text">Standardise processes &amp; gain commitment</p></div>
  <div class="step step--proactive"><div class="step__head">OWNERSHIP<br>CULTURE</div><p class="step__quote">“We prevent incidents”</p><p class="step__text">All team members engaged &amp; all risks controlled</p></div>
  <div class="step step--resilient"><div class="step__head">INTERDEPENDENT<br>CULTURE</div><p class="step__quote">“It’s how we do business.”</p><p class="step__text">Develop consistency &amp; fight complacency</p></div>

  <footer class="front-footer">BASED ON THE BRENMOOR INSTITUTE AND ALAN WHITCOMBE “HEADS AND HANDS” MODEL</footer>
</section>

<!-- Back page -->
<section class="page page--back">
  <div class="back-title">SAFETY CULTURE MATURITY LADDER</div>

  <div class="trait-col trait-col--vulnerable">
    <ul class="bullets">
      <li><span class="lead">Toxic / No care culture</span>
        <ul><li>Apathy / resistance</li><li>Near misses not considered</li><li>Negligence</li><li>Dishonesty</li><li>Hiding of incidents</li><li>Serious injury/health risks are unseen or ignored</li><li>Unfair disciplinary actions</li></ul></li>
      <li>No or little training</li>
      <li>Poor or no communication</li>
      <li>Production at almost any cost</li>
      <li>“Just get it done” attitude or blatantly unsafe</li>
    </ul>
    <p class="summary">Accept that incidents happen</p>
  </div>

  <div class="trait-col trait-col--reactive">
    <ul class="bullets">
      <li><span class="lead">Blame culture</span>
        <ul><li>Dependent on natural instincts</li><li>Accept need to care</li><li>Some near miss reporting</li><li>Some window dressing e.g. pre-inspection cleanups and light duty</li><li>Disciplinary action</li></ul></li>
      <li>Minimum / inconsistent training</li>
      <li>Some communication on a need to know basis</li>
    </ul>
    <p class="summary">Prevent a similar incident</p>
  </div>

  <div class="trait-col trait-col--compliant">
    <ul class="bullets">
      <li><span class="lead">Compliance culture</span>
        <ul><li>Supervision dependent</li><li>Some participation</li><li>Near miss discussions</li></ul></li>
      <li>Acceptable training / awareness</li>
      <li>Established and good communication channels</li>
      <li>Regular people involvement and focus</li>
    </ul>
    <p class="summary">Prevent incidents before they occur</p>
  </div>

  <div class="trait-col trait-col--proactive">
    <ul class="bullets">
      <li><span class="lead">Independent &amp; personal ownership culture</span>
        <ul><li>Involvement at all levels</li><li>Near miss involvement</li></ul></li>
      <li>High level of training / awareness</li>
      <li>Communication at a high level hiding nothing</li>
    </ul>
    <p class="summary">Improve the systems</p>
  </div>

  <div class="trait-col trait-col--resilient">
    <ul class="bullets">
      <li><span class="lead">Interdependent teams culture</span></li>
      <li>Way of life</li>
      <li>Comes natural</li>
      <li>Personal involvement by all to manage risks well and prevent incidents</li>
      <li>Authentic communication throughout culture</li>
    </ul>
    <p class="summary" style="color:var(--teal)">Way we do business</p>
  </div>

  <svg class="tier-art" width="689" height="483" viewBox="0 0 689 483" aria-hidden="true">
    <polygon points="15,266 143,252 143,483 15,483" fill="var(--blue)"/>
    <polygon points="147,249 275,233 275,483 147,483" fill="var(--crimson)"/>
    <polygon points="280,230 408,212 408,483 280,483" fill="var(--orange)"/>
    <polygon points="412,210 540,190 540,483 412,483" fill="var(--teal)"/>
    <polygon points="545,188 673,168 673,483 545,483" fill="var(--charcoal)"/>
    <circle cx="77" cy="257" r="17" fill="var(--white)" stroke="var(--blue)" stroke-width="1.5"/><use href="#icon-shield" x="65" y="245" width="24" height="24" color="var(--blue)"/>
    <circle cx="210" cy="241" r="17" fill="var(--white)" stroke="var(--crimson)" stroke-width="1.5"/><use href="#icon-cycle" x="198" y="229" width="24" height="24" color="var(--crimson)"/>
    <circle cx="344" cy="220" r="17" fill="var(--white)" stroke="var(--orange)" stroke-width="1.5"/><use href="#icon-doc" x="332" y="208" width="24" height="24" color="var(--orange)"/>
    <circle cx="476" cy="197" r="17" fill="var(--white)" stroke="var(--teal)" stroke-width="1.5"/><use href="#icon-bulb" x="464" y="185" width="24" height="24" color="var(--teal)"/>
    <circle cx="611" cy="177" r="17" fill="var(--white)" stroke="var(--charcoal)" stroke-width="1.5"/><use href="#icon-converge" x="599" y="165" width="24" height="24" color="var(--charcoal)"/>
  </svg>

  <div class="tier tier--vulnerable">
    <div class="tier__name" style="top:280px">VULNERABLE</div>
    <ul class="bullets" style="top:302px">
      <li>Reactive or unresponsive approach</li><li>No OHS systems</li><li>No risk assessment</li><li>Legal non compliance</li><li>Accept equipment / process decay</li><li>Only fix when broken / unsafe repairs</li><li>Reports are shelved / used irresponsibly</li><li>No or poor investigation</li><li>No monitoring / audits</li><li>Permit non-compliance</li><li>Potential illegal practices</li>
    </ul>
  </div>

  <div class="tier tier--reactive">
    <div class="tier__name" style="top:262px">REACTIVE</div>
    <ul class="bullets" style="top:279px">
      <li>Administrator driven</li><li>Loose systems, elements of an OHS Management System</li><li><b>Reactive risk assessment and control</b></li><li>Minimum legal compliance</li><li>Apply PPE as a way of eliminating exposure</li><li><b>Incident investigation but limited analysis</b>
        <ul><li>Focus on what happened</li><li>No systems focus</li><li>Human faults occur</li></ul></li>
      <li>Ad hoc monitoring / audits</li><li>No occupational hygiene or health initiatives</li><li>Reactive medical monitoring</li><li>Monitoring as per regulations</li>
    </ul>
  </div>

  <div class="tier tier--compliant">
    <div class="tier__name" style="top:242px">COMPLIANT</div>
    <ul class="bullets" style="top:260px">
      <li>OHS coordinator driven</li><li>OHS standards system and ISO 9002 or equivalent</li><li><b>Risk assessment through existing systems</b></li><li>Total legal compliance goal</li><li>Strictly enforced the use of PPE where required (knowing risk)</li><li><b>Causal incident analysis based on events potential</b></li><li>Info sharing from events</li><li>Planned occupational hygiene / environmental monitoring</li><li>Periodical medical examinations</li><li><b>Planned monitoring / audits</b></li><li>Safety meetings and talks</li><li>Some task observations</li>
    </ul>
  </div>

  <div class="tier tier--proactive">
    <div class="tier__name" style="top:221px">PROACTIVE</div>
    <ul class="bullets" style="top:241px">
      <li>Committed leadership at all levels</li><li>Line driven systems improvement</li><li>ISO 14001 and ISO 45001</li><li><b>Pro-active formal risk management</b></li><li>Beyond legal compliance</li><li>Seek to actively engineer out process / equipment inadequacies</li><li><b>Incident learnings shared with all levels</b></li><li>Well designed plans / procedures</li><li><b>Focus on adhering to site plans and procedures</b></li><li>Integrated audits</li><li>Peer evaluations and discussion</li>
    </ul>
  </div>

  <div class="tier tier--resilient">
    <div class="tier__name" style="top:200px">RESILIENT</div>
    <ul class="bullets" style="top:222px">
      <li>Individually internalized</li><li>Inspiring genuine leadership</li><li>No silo thinking or actions</li><li>All staff active, positive, respected, speaking up</li><li>Excellent equipment, ultra-organised</li><li>Integrated management systems</li><li><b>Risk management cycle integrated into all systems</b></li><li>Self regulating style</li><li><b>Eliminate &amp; prevent problems before they occur</b></li><li>All threats considered in decision-making</li><li><b>Continually improving through external evaluation / auditing</b></li><li>Multiple positive performance indicators drive PDCA cycle</li>
    </ul>
  </div>
</section>

</body>
</html>
```